A Postcard Design for a Vintage/Handcrafted Fair/Event called "The Hollow Mill Bazaar"

What is The Hollow Mill Bazaar? It’s an indoor/outdoor Market with the feel of a vintage/village fair (like mini shops) with over 25 handpicked vendors. For example: They could be selling…Vintage, repurposed, chippy, rusty, faded, patina, furniture, antique, jewelry, Spring Décor, architectural, outdoor furnishing, garden art, handcrafted goods. The Setting again is indoor/outdoor. Outdoor is under covered tents. Indoor is in 2 pole sheds/barn. The surrounding around these tents and pole sheds are lots of woods and hay/corn fields. Truly out in the country.

Sponsored by “A Tiny RWB”.
FB: facebook.com/atinyrwb
E-Mail: atinyrwb@mailbrook.example

Date of Event:
Friday, April 28th 9am – 7pm
Saturday, April 29th 9am – 5pm

Address of the Event:
48736 117th St SE
Elk River, MN 55330

This event is FREE of charge.

Although I’m open to any and all creative ideas I would appreciate if you can keep to the “Vintage/Rustic” theme (this is important…vintage like – very important). I want potential customers to look at this postcard and say “this looks fun we should go” just based off your design. Your design should be “Spring” as well. This event is in the Spring time.

The only idea I have that I thought might be a good catch would be using a swing somehow in the design and perhaps saying something like…”Swing into Spring as your browse row after row of marvelous vintage and creative handmade goods from over 25 vendors.” (This could be put on the back of the postcard if needed. Keeping the front of the postcard simple and eye catching with the name of the event (The Hollow Mill Bazaar) and the dates and address. THINK SPRING though when you are designing.

Again, I’m very open to all of your creative ideas and your vision you see based on my description. You do not need to use the “swing idea” if your creative brain takes you a different direction.

Other options I put in pictures to give you some ideas of what I liked. These again are just ideas. I am open to your creative ideas. I like old bikes, old windows, old barns, vintage trucks, rope swings, vintage suitcases...I even saw a beautiful big tree that would be great as a back drop and a vintage sofa under it....or a spring/garden vignette. Banners and Bunting is vintage like and acceptable if you want. I like old barns as well. Again the setting is in pole sheds with lots of woods and fields around. Hope this will get your creative juices flowing :). lol. I'm open to all your ideas. Thank you so much for helping me creative my postcard.

Target Market(s)

The General Public

Industry/Entity Type

Event

Requirements
Must have
• Event Name: The Hollow Mill Bazaar
• Sponsored by “A Tiny RWB”.
• FB: facebook.com/atinyrwb
• E-Mail: atinyrwb@mailbrook.example
• Date of Event:
• Friday, April 28th 9am – 7pm
• Saturday, April 29th 9am – 5pm
• Address of the Event:
• 48736 117th St SE
• Elk River, MN 55330

```html
<!DOCTYPE html>
<html lang="en">
<head>
<meta charset="utf-8">
<title>The Hollow Mill Bazaar – Postcard</title>
<link rel="stylesheet" href="https://fonts.googleapis.com/css2?family=Oswald:wght@300;400&family=Pinyon+Script&family=Satisfy&display=swap">
<style>
  :root {
    --backdrop: #000000;
    --paper: #eaf2e7;
    --paper-edge: #e2ebdf;
    --ink-green: #1f3b31;
    --ink-dark: #2a2f2b;
    --ink-brown: #7a3a18;
    --rule: #9aa39c;
    --bloom-red: #d9474a;
    --bloom-yellow: #f1d54a;
    --leaf-green: #5fae57;
  }
  * { box-sizing: border-box; margin: 0; padding: 0; }
  html, body { width: 960px; height: 1200px; overflow: hidden; background: var(--backdrop); }
  .canvas { position: relative; width: 960px; height: 1200px; background: var(--backdrop); }

  .postcard {
    position: absolute; left: 162px; width: 645px; height: 499px;
    background: radial-gradient(ellipse at 50% 40%, var(--paper) 60%, var(--paper-edge) 100%);
    overflow: hidden; color: var(--ink-dark);
    font-family: "Oswald", "Arial Narrow", sans-serif; font-weight: 300;
  }
  .postcard--front { top: 70px; }
  .postcard--back { top: 643px; }

  .center { position: absolute; left: 0; width: 100%; text-align: center; }

  .event-title {
    top: 36px; font-family: "Pinyon Script", cursive; font-weight: 400;
    font-size: 54px; line-height: 1; color: var(--ink-green);
  }
  .sponsor { top: 132px; display: flex; justify-content: center; align-items: center; gap: 12px;
    font-size: 18px; color: var(--ink-green); font-weight: 400; }
  .sponsor__name { display: flex; align-items: center; gap: 6px; font-size: 18px; font-weight: 400; color: var(--ink-brown); }
  .sponsor__dot { width: 14px; height: 14px; border-radius: 50%; background: var(--ink-brown); }

  .event-dates { top: 192px; font-size: 16px; letter-spacing: 0.1px; }
  .event-dates .sep { margin: 0 12px; }
  .rule { position: absolute; left: 180px; width: 278px; height: 1px; background: var(--rule); }
  .rule--upper { top: 225px; }
  .rule--lower { top: 259px; }
  .event-address { top: 231px; font-size: 15px; }

  .contact-row { top: 272px; display: flex; justify-content: center; gap: 18px; font-size: 13px; }
  .contact { display: inline-flex; align-items: center; gap: 5px; }
  .icon-circle { display: inline-block; width: 14px; height: 14px; border-radius: 50%; background: var(--ink-green); }

  .tagline { top: 318px; font-family: "Satisfy", cursive; font-size: 22px; color: var(--ink-brown); }

  .meadow {
    position: absolute; bottom: 0;
    background: linear-gradient(180deg, rgba(234,242,231,0) 0%, rgba(241,213,74,0.55) 35%, rgba(217,71,74,0.55) 60%, rgba(95,174,87,0.75) 100%);
  }
  .postcard--front .meadow { left: 0; width: 100%; height: 150px; }
  .postcard--back .meadow { left: 0; width: 320px; height: 138px; }

  .invitation {
    position: absolute; left: 41px; top: 34px; width: 290px;
    font-family: "Satisfy", cursive; font-size: 24px; line-height: 34px; color: var(--ink-green);
  }
  .back-contacts { position: absolute; left: 41px; top: 240px; font-size: 17px; color: var(--ink-green); font-weight: 400; }
  .back-contacts .contact { margin-bottom: 13px; gap: 9px; display: flex; }
  .back-contacts .icon-circle { width: 22px; height: 22px; }

  .stamp-box { position: absolute; left: 514px; top: 29px; width: 99px; height: 112px; border: 1px solid #7d857f; }
  .address-line { position: absolute; left: 358px; width: 255px; height: 1px; background: var(--rule); }
</style>
</head>
<body>
<main class="canvas">

  <section class="postcard postcard--front" aria-label="Postcard front">
    <h1 class="center event-title">The Hollow Mill Bazaar</h1>
    <div class="center sponsor">
      <span>Sponsored by</span>
      <span class="sponsor__name"><span class="sponsor__dot"></span>A Tiny RWB</span>
    </div>
    <p class="center event-dates">Friday, April 28th 9am – 7pm<span class="sep">|</span>Saturday, April 29th 9am – 5pm</p>
    <div class="rule rule--upper"></div>
    <p class="center event-address">48736 117th St SE Elk River, MN 55330</p>
    <div class="rule rule--lower"></div>
    <div class="center contact-row">
      <span class="contact">
        <svg width="16" height="11" viewBox="0 0 16 11" aria-hidden="true"><rect x="0.5" y="0.5" width="15" height="10" fill="var(--ink-green)"/><path d="M0.5 0.5 L8 6 L15.5 0.5" fill="none" stroke="var(--paper)" stroke-width="1.2"/></svg>
        atinyrwb@mailbrook.example
      </span>
      <span class="contact"><span class="icon-circle"></span>/atinyrwb</span>
    </div>
    <p class="center tagline">Shop – Laugh – Eat – REPEAT!</p>
    <div class="meadow" role="img" aria-label="Watercolour spring meadow of red poppies and yellow blooms with green stems, two bumblebees and a ladybird"></div>
  </section>

  <section class="postcard postcard--back" aria-label="Postcard back">
    <p class="invitation">Swing into Spring as your browse row after row of marvelous vintage and creative handmade goods from over 25 vendors.</p>
    <div class="back-contacts">
      <span class="contact">
        <svg width="22" height="15" viewBox="0 0 16 11" aria-hidden="true"><rect x="0.5" y="0.5" width="15" height="10" fill="var(--ink-green)"/><path d="M0.5 0.5 L8 6 L15.5 0.5" fill="none" stroke="var(--paper)" stroke-width="1.2"/></svg>
        atinyrwb@mailbrook.example
      </span>
      <span class="contact"><span class="icon-circle"></span>/atinyrwb</span>
    </div>
    <div class="stamp-box"></div>
    <div class="address-line" style="top:301px"></div>
    <div class="address-line" style="top:339px"></div>
    <div class="address-line" style="top:378px"></div>
    <div class="address-line" style="top:416px"></div>
    <div class="meadow" role="img" aria-label="Watercolour cluster of red poppies and yellow blooms with a ladybird on green stems"></div>
  </section>

</main>
</body>
</html>
```